Postcard Design

Hoofmere Ftness Center is a state of the art equine rehabilitation and fitness center. We offer a wide variety of options to get your equine partner in tip top performing condition. Whether is swimming in or 11 foot deep pool or exercising in the squatted, we provide a personalized program for your special horse. Some other services offered are StallAir breathing treatments, pulso drift and gallotone.
Updates
Project Deadline Extended Reason: Since the project was started we have opened for business and I have pictures using my equipment at our place of business that I would like to add to the project to be used. I have also received my logo design from one of your designers that I would like added to this project. Added Tuesday, March 15, 2016
Industry/Entity Type
Fitness
Look and feel
Each slider illustrates characteristics of the customer's brand and the style your logo design should communicate.

```html
<!DOCTYPE html>
<html lang="en">
<head>
<meta charset="utf-8">
<title>Hoofmere Fitness Center – Postcard</title>
<link href="https://fonts.googleapis.com/css2?family=Playfair+Display:wght@900&family=EB+Garamond:ital@1&family=Tinos:wght@400;700&display=swap" rel="stylesheet">
<style>
  :root {
    --stage: #2b2b2b;
    --card-black: #000000;
    --card-white: #ffffff;
    --ink-white: #ffffff;
    --ink-gold: #f2b326;
    --rule: #8a8a8a;
    --art-teal: #3fb6c8;
    --art-violet: #6b3fa0;
    --art-yellow: #f4c21f;
    --art-orange: #ef7d22;
    --art-red: #c8233a;
    --water: #5fb7c6;
    --horse-dark: #3a2a22;
  }
  * { margin: 0; padding: 0; box-sizing: border-box; }
  html, body { width: 1200px; height: 1173px; overflow: hidden; background: var(--stage); }
  .canvas { position: relative; width: 1200px; height: 1173px; }

  .card { position: absolute; overflow: hidden; }
  .card--front { left: 219px; top: 23px; width: 711px; height: 547px; background: var(--card-black); }
  .card--back { left: 218px; top: 601px; width: 710px; height: 546px; background: var(--card-white); }

  .wordmark {
    position: absolute; font-family: "Playfair Display", Georgia, serif; font-weight: 900;
    color: var(--ink-white); letter-spacing: 2px; line-height: 1; white-space: nowrap;
  }
  .subtitle {
    position: absolute; font-family: "Tinos", "Times New Roman", serif; font-weight: 700;
    color: var(--ink-white); line-height: 1; white-space: nowrap; letter-spacing: 0.5px;
  }
  .tagline {
    position: absolute; font-family: "EB Garamond", Garamond, serif; font-style: italic;
    color: var(--ink-gold); text-align: center;
  }
  .body-copy {
    position: absolute; font-family: "Tinos", "Times New Roman", serif;
    color: var(--ink-white); text-align: center;
  }

  /* front */
  .front-art {
    position: absolute; left: 0; top: 0; width: 462px; height: 547px;
    background: radial-gradient(ellipse at 55% 45%, var(--art-teal) 0%, var(--art-violet) 30%, var(--art-yellow) 55%, var(--art-orange) 72%, var(--art-red) 85%, var(--card-black) 100%);
    clip-path: polygon(20% 0, 60% 0, 80% 35%, 100% 70%, 96% 92%, 70% 100%, 0 100%, 0 5%);
  }
  .card--front .wordmark { right: 36px; top: 44px; font-size: 48px; }
  .card--front .subtitle { right: 36px; top: 100px; font-size: 38px; }
  .card--front .tagline { left: 410px; width: 260px; top: 168px; font-size: 31px; line-height: 34.5px; }
  .card--front .body-copy { left: 414px; width: 240px; top: 346px; font-size: 20px; line-height: 25.6px; }

  /* back */
  .back-panel { position: absolute; left: 0; top: 0; width: 350px; height: 546px; background: var(--card-black); }
  .card--back .wordmark { left: 17px; top: 18px; font-size: 46px; }
  .card--back .subtitle { left: 18px; top: 67px; font-size: 27px; }
  .card--back .tagline { left: 10px; width: 336px; top: 96px; font-size: 19px; line-height: 22px; }
  .card--back .body-copy { left: 28px; width: 300px; top: 153px; font-size: 15.5px; line-height: 20.5px; }
  .back-art {
    position: absolute; left: 0; top: 318px; width: 160px; height: 228px;
    background: linear-gradient(150deg, var(--art-teal) 0%, var(--art-violet) 35%, var(--art-yellow) 65%, var(--art-orange) 85%, var(--art-red) 100%);
    clip-path: polygon(10% 0, 45% 5%, 70% 40%, 100% 80%, 90% 100%, 0 100%, 0 5%);
  }
  .back-photo {
    position: absolute; left: 139px; top: 321px; width: 196px; height: 196px; border-radius: 50%;
    background: radial-gradient(circle at 50% 40%, var(--horse-dark) 0%, var(--horse-dark) 22%, var(--water) 55%, #9fd6df 100%);
  }
  .divider { position: absolute; left: 355px; top: 87px; width: 1px; height: 425px; background: var(--rule); }
  .stamp-box { position: absolute; left: 603px; top: 25px; width: 88px; height: 102px; border: 1px solid var(--rule); }
  .address-line { position: absolute; left: 389px; width: 270px; height: 1px; background: var(--rule); }
</style>
</head>
<body>
<div class="canvas">

  <section class="card card--front">
    <div class="front-art" role="img" aria-label="Colorful painted horse head with flowing rainbow mane"></div>
    <h1 class="wordmark">Hoofmere</h1>
    <p class="subtitle">Fitness Center</p>
    <p class="tagline">is a state of<br>the art equine<br>rehabilitation and<br>fitness center</p>
    <p class="body-copy">We offer a wide variety<br>of options to get<br>your equine<br>partner in tip top<br>performing<br>condition.</p>
  </section>

  <section class="card card--back">
    <div class="back-panel">
      <h2 class="wordmark">Hoofmere</h2>
      <p class="subtitle">Fitness Center</p>
      <p class="tagline">is a state of the art equine rehabilitation and<br>fitness center</p>
      <p class="body-copy">Whether is swimming in or<br>11 foot deep pool or<br>exercising in the squatted,<br>we provide a personalized<br>program for your special horse.<br>StallAir breathing<br>treatments, pulso drift and gallotone.</p>
      <div class="back-art" role="img" aria-label="Colorful painted horse head"></div>
      <div class="back-photo" role="img" aria-label="Photo of a dark horse standing in a swimming pool"></div>
    </div>
    <div class="divider"></div>
    <div class="stamp-box"></div>
    <div class="address-line" style="top:334px"></div>
    <div class="address-line" style="top:389px"></div>
    <div class="address-line" style="top:444px"></div>
  </section>

</div>
</body>
</html>
```